Customer Dashboard Design for Email Security SaaS

Mailbrook is a commercial email spam filter offered as a SaaS product, built and operated by a small German hosting provider. It protects business email accounts against spam, phishing, scam, and viruses using a multilayer filtering pipeline that combines traditional spam detection with AI-powered classification. The product runs entirely on German infrastructure, ensuring data sovereignty for European customers.

We need a complete redesign of the customer-facing dashboard. This is the web application where paying customers manage their email filtering: view their mail log, check quarantined emails, manage allow/blocklists, configure their settings, and handle their subscription. It is the primary touchpoint between Mailbrook and its customers.

Our customers are system administrators, IT managers at small-to-medium businesses, and operators of small hosting providers. They are technically competent but not designers. They expect professional, efficient tools that respect their time. They typically manage 10–500 email accounts and check the dashboard a few times per week, with heavier use during spam incidents.

We have attached the current mockups which really need to be replaced with something good looking.

Target Market(s)

System administrators, IT managers at small-to-medium businesses, and operators of small hosting providers.

Industry/Entity Type

SaaS

Number of Pages Required

5+ page

```html
<!DOCTYPE html>
<html lang="de">
<head>
<meta charset="utf-8">
<title>Mailbrook – Dashboard</title>
<link href="https://fonts.googleapis.com/css2?family=Lexend:wght@300;400;500;600&display=swap" rel="stylesheet">
<style>
  :root {
    --bg-top: #1a1a1a;
    --bg-bottom: #1d2a22;
    --panel: #121212;
    --card: #252527;
    --card-highlight: #1b2a22;
    --green: #3f8f63;
    --green-line: #2dbb7a;
    --green-soft: #1f4a33;
    --green-text: #4fbf82;
    --red-line: #d93636;
    --orange-line: #ef7a1a;
    --text: #ffffff;
    --text-muted: #d8d8d8;
    --grid: #3a3a3a;
    --divider: #3a3a3a;
  }
  * { box-sizing: border-box; margin: 0; padding: 0; }
  html, body { width: 1200px; height: 1126px; overflow: hidden; }
  body {
    font-family: "Lexend", sans-serif;
    color: var(--text);
    background: linear-gradient(180deg, var(--bg-top) 0%, #1a1f1c 55%, var(--bg-bottom) 100%);
  }
  .stage {
    position: relative;
    width: 1280px; height: 1201px;
    transform: scale(.9375);
    transform-origin: 0 0;
  }
  .topbar {
    position: absolute; left: 0; top: 0; width: 1280px; height: 76px;
    border-bottom: 1px solid var(--divider);
  }
  .brand { position: absolute; left: 64px; top: 14px; display: flex; align-items: center; gap: 13px; }
  .brand-mark { width: 46px; height: 46px; border-radius: 10px; background: var(--green); }
  .brand-name { font-size: 23px; font-weight: 500; letter-spacing: -.2px; }
  .avatar {
    position: absolute; left: 1030px; top: 16px; width: 45px; height: 45px; border-radius: 50%;
    background: radial-gradient(circle at 50% 40%, #c89a7a, #6b4a36 70%);
    border: 2px solid #f0f0f0;
  }
  .online-dot { position: absolute; left: 1067px; top: 17px; width: 10px; height: 10px; border-radius: 50%; background: #22d35a; }
  .logout {
    position: absolute; left: 1095px; top: 22px; width: 32px; height: 32px; border-radius: 50%;
    background: #fff; display: flex; align-items: center; justify-content: center;
  }
  .theme-toggle {
    position: absolute; left: 1143px; top: 18px; width: 72px; height: 40px; border-radius: 20px;
    background: #2b2b2d; display: flex; align-items: center; padding: 0 6px; gap: 8px;
  }
  .theme-knob { width: 30px; height: 30px; border-radius: 50%; background: #4b4fc8; display: flex; align-items: center; justify-content: center; }

  .sidenav {
    position: absolute; left: 36px; top: 112px; width: 86px; height: 555px;
    border: 1.5px solid var(--green); border-radius: 28px;
    background: linear-gradient(180deg, #1c2a22, #16231c);
    padding: 8px 8px;
  }
  .nav-item { height: 69px; display: flex; align-items: center; justify-content: center; border-bottom: 1px solid #3f5c4b; }
  .nav-item:last-child { border-bottom: none; }
  .nav-item svg { width: 30px; height: 30px; fill: none; stroke: #fff; stroke-width: 1.4; stroke-linejoin: round; stroke-linecap: round; }

  .panel { position: absolute; left: 137px; width: 1103px; background: var(--panel); border-radius: 26px; }
  .overview { top: 112px; height: 416px; }
  .greeting { position: absolute; left: 24px; top: 19px; font-size: 22px; font-weight: 400; }
  .mode-badge {
    position: absolute; left: 24px; top: 57px; height: 24px; padding: 0 13px;
    border: 1px solid var(--green-text); border-radius: 12px;
    color: var(--green-text); font-size: 10.5px; font-weight: 300; line-height: 22px;
  }
  .stat { position: absolute; background: var(--card); border-radius: 16px; }
  .stat.lead { background: var(--card-highlight); }
  .stat-label { position: absolute; left: 22px; font-size: 16px; font-weight: 400; }
  .stat-value { position: absolute; left: 20px; font-weight: 400; }
  .stat-note { position: absolute; left: 22px; font-size: 11.5px; font-weight: 400; }
  .big .stat-label { top: 16px; }
  .big .stat-value { top: 40px; font-size: 50px; }
  .big .stat-note { top: 120px; }
  .lead .stat-value { font-size: 58px; top: 38px; font-weight: 500; }
  .small .stat-label { left: 27px; top: 18px; font-size: 15px; }
  .small .stat-value { left: 27px; top: 44px; font-size: 30px; }
  .small .stat-note { left: 27px; top: 92px; font-size: 11px; }

  .volume { top: 548px; height: 502px; }
  .volume-title { position: absolute; left: 25px; top: 26px; font-size: 22px; font-weight: 400; }
  .range-switch {
    position: absolute; left: 927px; top: 18px; width: 152px; height: 42px; border-radius: 21px;
    background: #1e1e1e; display: flex; align-items: center;
  }
  .range-switch span { flex: 1; text-align: center; font-size: 15px; height: 42px; line-height: 42px; border-radius: 21px; }
  .range-switch .active { background: var(--green); }
  .chart { position: absolute; left: 0; top: 0; width: 1103px; height: 502px; }
  .chart text { fill: #e6e6e6; font-family: "Lexend", sans-serif; font-size: 12.5px; }

  .action {
    position: absolute; top: 1075px; width: 534px; height: 75px; border-radius: 24px;
    text-align: center; padding-top: 9px;
  }
  .action.primary { left: 137px; background: #22503a; }
  .action.secondary { left: 703px; background: #1b3427; }
  .action-title { font-size: 24px; font-weight: 400; }
  .action-sub { font-size: 15.5px; font-weight: 300; margin-top: 4px; }
</style>
</head>
<body>
<div class="stage">

  <header class="topbar">
    <div class="brand"><div class="brand-mark"></div><span class="brand-name">Mailbrook</span></div>
    <div class="avatar" role="img" aria-label="Profilbild des angemeldeten Nutzers"></div>
    <div class="online-dot"></div>
    <div class="logout">
      <svg width="20" height="20" viewBox="0 0 20 20" fill="none" stroke="#111" stroke-width="2.2" stroke-linecap="round" stroke-linejoin="round">
        <path d="M8 4H5a1 1 0 0 0-1 1v10a1 1 0 0 0 1 1h3"/><path d="M9 10h8M14 7l3 3-3 3"/>
      </svg>
    </div>
    <div class="theme-toggle">
      <div class="theme-knob">
        <svg width="18" height="18" viewBox="0 0 18 18"><path d="M12 2a7 7 0 1 0 4 12A6 6 0 0 1 12 2z" fill="#f5c23a"/></svg>
      </div>
      <svg width="22" height="22" viewBox="0 0 22 22" stroke="#fff" stroke-width="1.8" stroke-linecap="round">
        <circle cx="11" cy="11" r="4" fill="#fff"/><path d="M11 1v3M11 18v3M1 11h3M18 11h3M4 4l2 2M16 16l2 2M4 18l2-2M16 6l2-2"/>
      </svg>
    </div>
  </header>

  <nav class="sidenav">
    <div class="nav-item"><svg viewBox="0 0 30 30"><rect x="4" y="4" width="9" height="12" rx="1"/><rect x="17" y="4" width="9" height="7" rx="1"/><rect x="4" y="19" width="9" height="7" rx="1"/><rect x="17" y="14" width="9" height="12" rx="1"/></svg></div>
    <div class="nav-item"><svg viewBox="0 0 30 30"><rect x="3" y="8" width="22" height="16" rx="1"/><path d="M3 9l11 8 11-8"/><path d="M7 4h20v15"/></svg></div>
    <div class="nav-item"><svg viewBox="0 0 30 30"><path d="M4 13h16v12H4z"/><path d="M4 13l8 6 8-6"/><path d="M20 13V5h6v5h-6"/><circle cx="23" cy="20" r="2"/></svg></div>
    <div class="nav-item"><svg viewBox="0 0 30 30"><rect x="6" y="4" width="18" height="23" rx="1"/><circle cx="11" cy="9" r="3"/><path d="M16 9h5M10 15h11M10 19h11M10 23h8"/></svg></div>
    <div class="nav-item"><svg viewBox="0 0 30 30"><circle cx="14" cy="8" r="4.5"/><path d="M5 26c0-7 4-11 9-11"/><circle cx="19" cy="21" r="6"/><path d="M15 25l8-8"/></svg></div>
    <div class="nav-item"><svg viewBox="0 0 30 30"><rect x="3" y="4" width="24" height="22"/><path d="M3 9h24M8 9v17M13 9v17M18 9v17M23 9v17"/><path d="M10 14l6 7M16 14l-6 7"/></svg></div>
    <div class="nav-item"><svg viewBox="0 0 30 30"><circle cx="15" cy="15" r="4"/><path d="M15 3l2 3 3.5-1 .5 3.5 3.5 1-1 3.5 3 2-3 2 1 3.5-3.5 1-.5 3.5-3.5-1-2 3-2-3-3.5 1-.5-3.5-3.5-1 1-3.5-3-2 3-2-1-3.5 3.5-1 .5-3.5 3.5 1z"/></svg></div>
    <div class="nav-item"><svg viewBox="0 0 30 30"><path d="M5 9h15v17H5z"/><path d="M8 14h9M8 18h9M8 22h6"/><circle cx="22" cy="8" r="5"/><path d="M22 5.5v5M20.5 7h2.5a1 1 0 0 1 0 2h-1.5"/></svg></div>
  </nav>

  <section class="panel overview">
    <h1 class="greeting">Guten Morgen, Jonas</h1>
    <div class="mode-badge">Beobachtungsmodus - Mails werden analysiert aber nicht blockiert</div>

    <div class="stat big lead" style="left:25px; top:108px; width:562px; height:145px;">
      <div class="stat-label">Letzte 24 Stunden</div>
      <div class="stat-value">1.247</div>
      <div class="stat-note">849 Zugestelt&nbsp;&nbsp;398 abgefangen</div>
    </div>
    <div class="stat big" style="left:604px; top:108px; width:230px; height:145px;">
      <div class="stat-label" style="top:20px">7 Tage</div>
      <div class="stat-value">8.472</div>
      <div class="stat-note" style="top:108px">68% zugestelt</div>
    </div>
    <div class="stat big" style="left:847px; top:108px; width:230px; height:145px;">
      <div class="stat-label" style="top:20px">30 Tage</div>
      <div class="stat-value">34.902</div>
      <div class="stat-note" style="top:108px">71% zugestelt</div>
    </div>

    <div class="stat small" style="left:25px; top:266px; width:200px; height:125px;">
      <div class="stat-label">Spam blockiert</div><div class="stat-value">4,219</div><div class="stat-note">+12% ggu. Vormonat</div>
    </div>
    <div class="stat small" style="left:239px; top:266px; width:200px; height:125px;">
      <div class="stat-label">Phishing erkannt</div><div class="stat-value">145</div><div class="stat-note">+3 heute</div>
    </div>
    <div class="stat small" style="left:452px; top:266px; width:200px; height:125px;">
      <div class="stat-label">Viran abgefangen</div><div class="stat-value">12</div><div class="stat-note">0 heute</div>
    </div>
    <div class="stat small" style="left:666px; top:266px; width:200px; height:125px;">
      <div class="stat-label">Newsletter sortiert</div><div class="stat-value">145</div><div class="stat-note">34 heute</div>
    </div>
    <div class="stat small" style="left:879px; top:266px; width:200px; height:125px;">
      <div class="stat-label">In Quarantane</div><div class="stat-value">23</div><div class="stat-note">Uberprufung erforderlich</div>
    </div>
  </section>

  <section class="panel volume">
    <svg class="chart" viewBox="137 548 1103 502" aria-label="Liniendiagramm E-Mail-Volumen der letzten 7 Tage">
      <g stroke="var(--grid)" stroke-width="1">
        <line x1="205" y1="640" x2="205" y2="985"/><line x1="329" y1="640" x2="329" y2="985"/>
        <line x1="452" y1="640" x2="452" y2="985"/><line x1="697" y1="640" x2="697" y2="985"/>
        <line x1="820" y1="640" x2="820" y2="985"/><line x1="943" y1="640" x2="943" y2="985"/>
        <line x1="1066" y1="640" x2="1066" y2="985"/>
        <line x1="195" y1="985" x2="1100" y2="985" stroke="#555"/>
      </g>
      <line x1="575" y1="640" x2="575" y2="985" stroke="#fff" stroke-width="1.2"/>
      <g text-anchor="end">
        <text x="194" y="712">340</text><text x="194" y="779">255</text>
        <text x="194" y="849">170</text><text x="194" y="919">80</text><text x="186" y="989">0</text>
      </g>
      <g text-anchor="middle">
        <text x="225" y="1012">10 Mar</text><text x="326" y="1012">11 Mar</text>
        <text x="448" y="1012">12 Mar</text><text x="573" y="1012">13 Mar</text>
        <text x="693" y="1012">14 Mar</text><text x="827" y="1012">15 Mar</text>
        <text x="948" y="1012">16 Mar</text><text x="1073" y="1012">17 Mar</text>
      </g>
      <g fill="none" stroke-width="2.6" stroke-linecap="round">
        <path stroke="var(--green-line)" d="M205 750 C250 722 300 702 340 710 C375 716 390 728 398 738 C415 780 430 802 455 802 C485 802 505 775 520 748 C530 700 545 672 575 674 C595 678 600 685 615 695 C650 714 690 730 710 737 C720 742 740 743 765 743 C795 743 820 738 840 730 C855 720 870 710 900 699 C930 689 960 690 975 705 C995 730 1010 741 1030 739 C1045 738 1055 730 1065 722"/>
        <path stroke="var(--red-line)" d="M205 953 C260 945 300 944 340 945 C370 946 385 950 395 953 C420 961 450 962 480 957 C505 952 515 946 530 932 C545 922 560 918 575 918 C600 918 615 932 630 935 C660 942 690 946 730 938 C750 930 770 918 810 915 C840 913 860 920 880 932 C900 942 930 946 960 945 C1000 944 1040 942 1068 941"/>
        <path stroke="var(--orange-line)" d="M205 973 C260 972 320 972 370 973 C410 974 430 976 452 985 C490 981 540 977 575 977 C620 979 670 979 695 973 C730 968 780 962 810 964 C860 968 900 971 940 973 C990 976 1030 978 1066 980"/>
      </g>
      <circle cx="575" cy="674" r="3.5" fill="#fff" stroke="var(--green-line)" stroke-width="1.5"/>
      <circle cx="575" cy="918" r="3.5" fill="#fff" stroke="var(--red-line)" stroke-width="1.5"/>
      <circle cx="575" cy="977" r="3.5" fill="var(--orange-line)" stroke="#fff" stroke-width="1"/>
    </svg>
    <h2 class="volume-title">E-Mail-Volumen</h2>
    <div class="range-switch"><span class="active">7 Tage</span><span>30 Tage</span></div>
  </section>

  <a class="action primary">
    <div class="action-title">Quarantane prufen</div>
    <div class="action-sub">23E- Mails warten auf Uberprufung</div>
  </a>
  <a class="action secondary">
    <div class="action-title">E-Mail-protokoll</div>
    <div class="action-sub">Alle verarbeiteten E-Mails durchuschen</div>
  </a>

</div>
</body>
</html>
```